We need a flyer where we promote a workshop to our members of the jewish community www.vbq-gemeinde.example . The workshop is calles "command in seven weeks presented by VBQ. We would like to see a flyer with the below text is used and also some pictures (attached). The flyer should come over as cool, fresh, innovative for a younger crowd so called young professionals (age 28-35).
TITLE.
"Command in Seven Weeks.
SUBTITLE.
Your systematic self-coaching roadmap to power and impact—and your future.”
TEXT.
Dr. Marcus L. Brandauer is the CEO Emeritus of Alpine Advisory Partners—he made an exit in 2013. He is the award-winning author of 8 books, including "Momentum-By-Design," "Speak Up or Fade" and "The Cantor and the Chairman.”
For the past 20 years he has taught leadership at Harwick University in New York and at KLB (Lindmoor University) to prepare future CEOs and other leaders in business, government , nonprofits and the military.
Now, in a process exclusively designed for VBQ’s next generation of emerging leaders, Marcus unpacks his leadership secrets in 3 action-packed labs—reduced to the max:
Lab 1. Command in Seven Weeks: The Summit Compass Model®. Self-Assessment. Self-Leadership: “The Lantern.” 5-Year Vision. 100-Day Catalytic Project.
Lab 2. Guiding Through Words. Relationship: Building Trust. Momentum-By-Design. Cockpit.
Lab 3. Debrief and Scale-Up. Sustainability. Action Tools.
Do you want to build your own future and a life you love? Do you want to jump-start that future and life over 100 days while learning a toolbox of leadership skills, networking with like-minded people—and even get some pizza? Then join us.
young professionals age 28-35

```html
<!DOCTYPE html>
<html lang="en">
<head>
<meta charset="utf-8">
<title>Command in Seven Weeks – VBQ Workshop Flyer</title>
<link href="https://fonts.googleapis.com/css2?family=Anton&family=Oswald:wght@400;500&family=Roboto:ital,wght@0,400;0,500;0,700;1,700&family=Roboto+Condensed:wght@700&display=swap" rel="stylesheet">
<style>
  :root {
    --page-bg: #c6dee6;
    --navy: #0c3a78;
    --ink-navy: #183263;
    --brand-blue: #2491bf;
    --panel-light: #e1ecee;
    --slate-dark: #2e3a52;
    --slate-mid: #4a5a78;
    --slate-light: #6b7a94;
    --lab-tag: #6fa8c0;
    --footer-panel: #a9ccd9;
    --logo-navy: #1f3a93;
    --text: #222;
    --cta-blue: #2070b0;
    --white: #fff;
  }
  * { margin: 0; padding: 0; box-sizing: border-box; }
  html, body { width: 848px; height: 1200px; overflow: hidden; background: var(--page-bg); }
  .canvas { position: relative; width: 848px; height: 1200px; font-family: "Roboto", Arial, sans-serif; color: var(--text); }
  .flyer { position: absolute; left: 46px; top: 65px; width: 757px; height: 1070px; background: var(--white); box-shadow: 0 2px 8px rgba(0,0,0,.18); }
  .shapes { position: absolute; left: 0; top: 0; width: 848px; height: 1200px; }
  .abs { position: absolute; }

  .subtitle { left: 0; top: 240px; width: 848px; font-weight: 500; font-size: 24px; line-height: 30px; color: var(--ink-navy); }
  .subtitle span { position: absolute; white-space: nowrap; }
  .role { left: 472px; top: 410px; font-size: 30px; font-weight: 500; color: var(--white); line-height: 36px; }

  .bio { left: 46px; top: 517px; width: 734px; font-size: 14px; line-height: 18.3px; color: var(--text); text-align: justify; }
  .bio-edge { float: left; width: 310px; height: 190px; shape-outside: polygon(0 0, 304px 0, 219px 190px, 0 190px); }
  .bio p + p { margin-top: 18px; }

  .speaker-tab { left: 373px; top: 482px; font-family: "Roboto Condensed", Arial, sans-serif; font-weight: 700; font-size: 15px; color: var(--white); letter-spacing: .2px; }

  .lab-tag { left: 87px; font-weight: 700; font-size: 18px; color: var(--white); line-height: 22px; }
  .lab-text { left: 178px; width: 610px; font-size: 14.6px; line-height: 18.5px; color: var(--ink-navy); }

  .cta { left: 73px; top: 975px; width: 730px; font-size: 15.2px; line-height: 20.4px; color: #111; }
  .cta strong { font-weight: 700; font-style: italic; color: var(--cta-blue); }

  .contact { font-size: 16px; color: var(--white); line-height: 20px; }
  .contact.phone { font-size: 20px; }
  .presented { left: 646px; top: 1114px; font-size: 14px; letter-spacing: 1px; color: #111; }
  .brand-name { left: 652px; top: 1042px; font-size: 56px; font-weight: 700; color: var(--logo-navy); line-height: 64px; }
</style>
</head>
<body>
<div class="canvas">
  <div class="flyer"></div>

  <svg class="shapes" viewBox="0 0 848 1200" xmlns="http://www.w3.org/2000/svg">
    <defs>
      <linearGradient id="portrait-tone" x1="0" y1="0" x2="0.4" y2="1">
        <stop offset="0" stop-color="#eef5f8"/>
        <stop offset=".45" stop-color="#b8cbd8"/>
        <stop offset="1" stop-color="#3f5577"/>
      </linearGradient>
      <linearGradient id="stage-tone" x1="0" y1="0" x2="0" y2="1">
        <stop offset="0" stop-color="#17171d"/>
        <stop offset=".55" stop-color="#3a1f2e"/>
        <stop offset="1" stop-color="#1d3f9a"/>
      </linearGradient>
      <linearGradient id="tab-fade" x1="0" y1="0" x2="1" y2="0">
        <stop offset="0" stop-color="#2491bf"/>
        <stop offset=".4" stop-color="#2491bf"/>
        <stop offset="1" stop-color="#2491bf" stop-opacity="0"/>
      </linearGradient>
      <linearGradient id="lab-fade" x1="0" y1="0" x2="1" y2="0">
        <stop offset="0" stop-color="#cfe2ec"/>
        <stop offset=".6" stop-color="#e6f0f5"/>
        <stop offset="1" stop-color="#ffffff"/>
      </linearGradient>
    </defs>

    <!-- hero -->
    <rect x="332" y="65" width="471" height="403" fill="var(--panel-light)"/>
    <rect x="46" y="65" width="286" height="403" fill="var(--navy)"/>
    <polygon points="62,79 285,79 455,448 62,448" fill="url(#portrait-tone)" role="img" aria-label="Portrait photo of the speaker in a blue suit, arms crossed"/>

    <text x="408" y="170" font-family="Anton, Impact, sans-serif" font-size="100" fill="var(--ink-navy)" textLength="374" lengthAdjust="spacingAndGlyphs">COMMAND</text>
    <text x="408" y="234" font-family="Anton, Impact, sans-serif" font-size="66" fill="var(--brand-blue)" textLength="362" lengthAdjust="spacingAndGlyphs">IN SEVEN WEEKS</text>

    <polygon points="420,352 803,352 803,401 444,401" fill="var(--brand-blue)"/>
    <text x="459" y="392" font-family="Oswald, Arial Narrow, sans-serif" font-size="40" fill="var(--white)" textLength="321" lengthAdjust="spacingAndGlyphs">DR. MARCUS L. BRANDAUER</text>

    <polygon points="444,401 578,401 556,448 457,448" fill="var(--slate-dark)"/>
    <polygon points="578,401 614,401 592,448 556,448" fill="var(--slate-mid)"/>
    <polygon points="622,401 650,401 665,448 600,448" fill="var(--slate-light)"/>
    <polygon points="640,401 650,401 665,448 628,448" fill="var(--slate-dark)"/>

    <!-- bio -->
    <polygon points="46,477 342,477 238,703 46,703" fill="url(#stage-tone)" role="img" aria-label="Photo of the speaker on a conference stage in front of a large audience"/>
    <polygon points="364,477 655,477 655,505 351,505" fill="url(#tab-fade)"/>

    <!-- labs banner -->
    <rect x="46" y="711" width="757" height="47" fill="var(--brand-blue)"/>
    <rect x="46" y="758" width="757" height="6" fill="#dbe9ef"/>
    <text x="72" y="744" font-family="Oswald, Arial Narrow, sans-serif" font-weight="500" font-size="25" fill="var(--white)" textLength="714" lengthAdjust="spacingAndGlyphs">Marcus unpacks his leadership secrets in 3 action-packed labs—reduced to the max:</text>

    <!-- labs -->
    <g class="lab-row">
      <polygon points="160,780 803,780 803,832 160,832 167,806" fill="url(#lab-fade)"/>
      <polygon points="72,780 155,780 162,806 155,832 72,832" fill="var(--lab-tag)"/>
    </g>
    <g class="lab-row">
      <polygon points="160,846 803,846 803,900 160,900 167,873" fill="url(#lab-fade)"/>
      <polygon points="72,846 155,846 162,873 155,900 72,900" fill="var(--lab-tag)"/>
    </g>
    <g class="lab-row">
      <polygon points="160,909 803,909 803,962 160,962 167,935" fill="url(#lab-fade)"/>
      <polygon points="72,909 155,909 162,935 155,962 72,962" fill="var(--lab-tag)"/>
    </g>

    <!-- footer -->
    <polygon points="617,1043 803,1043 803,1135 576,1135" fill="var(--footer-panel)"/>
    <polygon points="46,1062 601,1062 569,1135 46,1135" fill="var(--brand-blue)"/>
    <g class="icon-globe" fill="none" stroke="var(--white)" stroke-width="2.2">
      <circle cx="86.5" cy="1097.5" r="12.5"/>
      <ellipse cx="86.5" cy="1097.5" rx="5.5" ry="12.5"/>
      <line x1="74" y1="1097.5" x2="99" y2="1097.5"/>
      <path d="M76 1090.5 H97 M76 1104.5 H97"/>
    </g>
    <g class="icon-phone" fill="none" stroke="var(--white)" stroke-width="2.2">
      <rect x="320" y="1084" width="15" height="27" rx="2.5"/>
      <line x1="320" y1="1104" x2="335" y2="1104"/>
    </g>
  </svg>

  <div class="abs subtitle">
    <span style="left:416px;top:0">Your systematic self-coaching</span>
    <span style="left:432px;top:30px">roadmap to power and impact</span>
    <span style="left:447px;top:60px">and your future.</span>
  </div>
  <div class="abs role">CEO</div>

  <div class="abs speaker-tab">DR. MARCUS L. BRANDAUER</div>
  <div class="abs bio">
    <div class="bio-edge"></div>
    <p>is the CEO Emeritus of Alpine Advisory Partners—he made an exit in 2013. He is the award-winning author of 8 books, including "Momentum-By-Design," "Speak Up or Fade" and "The Cantor and the Chairman.” For the past 20 years he has taught leadership at Harwick University in New York and at KLB (Lindmoor University) to prepare future CEOs and other leaders in business, government , nonprofits and the military.</p>
    <p>Now, in a process exclusively designed for VBQ’s next generation of emerging leaders.</p>
  </div>

  <div class="abs lab-tag" style="top:795px">LAB 1</div>
  <div class="abs lab-text" style="top:788px">Command in Seven Weeks: The Summit Compass Model®. Self-Assessment. Self-Leadership: “The Lantern.” 5-Year Vision. 100-Day Catalytic Project.</div>
  <div class="abs lab-tag" style="top:862px">LAB 2</div>
  <div class="abs lab-text" style="top:864px">Guiding Through Words. Relationship: Building Trust. Momentum-By-Design. Cockpit.</div>
  <div class="abs lab-tag" style="top:924px">LAB 3</div>
  <div class="abs lab-text" style="top:926px">Debrief and Scale-Up. Sustainability. Action Tools.</div>

  <p class="abs cta">Do you want to build your own future and a life you love? Do you want to jump-start that future and life<br>over 100 days while learning a toolbox of leadership skills, networking with like-minded people—<br>and even get some pizza? <strong>THEN JOIN US.</strong></p>

  <div class="abs contact" style="left:111px;top:1088px">www.vbq-gemeinde.example</div>
  <div class="abs contact phone" style="left:342px;top:1087px">+41 44 555 01 90</div>
  <div class="abs brand-name">VBQ</div>
  <div class="abs presented">PRESENTED BY</div>
</div>
</body>
</html>
```